Etikett für ein Erfrischungsgetränk
Zielgruppe
Tarvelo ist ein Startup Unternehmen, welches in naher Zukunft ein
Hibiskus-Erfrischungsgetränk auf den Markt bringen möchte.
Die Zielgruppe ist jedermann. Ob jung oder alt.
Aufgabenstellung
Das Etikett einer 0,33 l Longneckflasche soll:
Erfrischend, Modern aber auch Zeitlos, Einzigartig, dezent wirken.
Das Logo soll hervorstehen und der Hintergrund dezent sein.
Vorderetikett: 76 mm breit, 86 mm hoch
Rücketikett: 55 mm breit, 75 mm hoch
Die Getränkfarbe ist rötlich.

```html
<!DOCTYPE html>
<html lang="de">
<head>
<meta charset="utf-8">
<title>Tarvelo – Etikett</title>
<link rel="stylesheet" href="https://fonts.googleapis.com/css2?family=Covered+By+Your+Grace&family=Arimo:wght@400&display=swap">
<style>
  :root {
    --paper: #ffffff;
    --sky: #3ec8ee;
    --mint: #6cc27a;
    --lime: #c4d33e;
    --brand: #b3137f;
    --ink: #111111;
    --splash: #ffffff;
    --petal: #e95a7e;
  }
  html, body {
    margin: 0;
    padding: 0;
    width: 1061px;
    height: 1200px;
    overflow: hidden;
    background: var(--paper);
  }
  .label {
    position: relative;
    width: 1061px;
    height: 1200px;
  }
  .label-shape {
    position: absolute;
    inset: 0;
  }
  .brand-name {
    position: absolute;
    left: 0;
    width: 1061px;
    top: 300px;
    margin: 0;
    text-align: center;
    font-family: "Covered By Your Grace", cursive;
    font-weight: 400;
    font-size: 240px;
    line-height: 1;
    color: var(--brand);
  }
  .splash {
    position: absolute;
    left: 150px;
    top: 680px;
    width: 620px;
    height: 190px;
    background: var(--splash);
    border-radius: 80px 60px 90px 70px / 70px 90px 60px 80px;
  }
  .flower {
    position: absolute;
    left: 722px;
    top: 690px;
    width: 220px;
    height: 225px;
    border-radius: 50%;
    background: radial-gradient(circle at 45% 55%, #b0163a 0 10%, var(--petal) 35%, #f490a8 100%);
  }
  .product-type {
    position: absolute;
    left: 233px;
    top: 745px;
    margin: 0;
    font-family: "Covered By Your Grace", cursive;
    font-weight: 400;
    font-size: 56px;
    line-height: 1;
    letter-spacing: 1px;
    color: var(--ink);
  }
  .product-detail {
    position: absolute;
    left: 253px;
    top: 814px;
    margin: 0;
    font-family: "Arimo", Arial, sans-serif;
    font-size: 25px;
    line-height: 1;
    color: var(--ink);
  }
</style>
</head>
<body>
  <main class="label">
    <svg class="label-shape" width="1061" height="1200" viewBox="0 0 1061 1200" role="img" aria-label="Etikettfläche mit dezentem, aquarellartigem Hintergrund mit Schnörkelmuster in Türkis, Grün und Gelb">
      <defs>
        <linearGradient id="label-wash" x1="0" y1="0" x2="0.2" y2="1">
          <stop offset="0" stop-color="var(--sky)"/>
          <stop offset="0.35" stop-color="#57c8c8"/>
          <stop offset="0.6" stop-color="var(--mint)"/>
          <stop offset="1" stop-color="var(--lime)"/>
        </linearGradient>
      </defs>
      <path d="M2 155 H215 C262 62 400 20 530 20 C660 20 800 62 845 155 H1057 V1198 H2 Z" fill="url(#label-wash)"/>
    </svg>

    <h1 class="brand-name">Tarvelo</h1>

    <div class="splash" role="img" aria-label="Weißer Farbklecks als Hintergrund für die Produktbezeichnung"></div>
    <div class="flower" role="img" aria-label="Illustration einer rosa Hibiskusblüte"></div>

    <p class="product-type">ERFRISCHUNGSGETRÄNK</p>
    <p class="product-detail">aus aufgebrühtem Hibiskustee</p>
  </main>
</body>
</html>
```